Postcard Design

we need a post card design for our company in worth, illinois called Velmoran Dental lab we would like to see designs that use the colors blue and gray. We are a dental lab specializing in removable dentures and partials. These particular post cards are emphasizing doing relines and repairs the same day our address is 4870 N corbett ave worth I'll. Phone 708-555-0142

Industry/Entity Type

Dental

```html
<!DOCTYPE html>
<html lang="en">
<head>
<meta charset="utf-8">
<title>Velmoran Dental Lab Postcard</title>
<link rel="stylesheet" href="https://fonts.googleapis.com/css2?family=Roboto+Condensed:ital,wght@0,400;0,700;0,900;1,900&family=Carlito:ital,wght@0,400;0,700;1,700&display=swap">
<style>
  :root {
    --navy: #1a4e8c;
    --sky: #1e9bd7;
    --tint: rgba(92, 185, 225, 0.55);
    --tint-strong: rgba(110, 195, 232, 0.8);
    --paper: #ffffff;
    --page: #ffffff;
    --ink: #1f1f1f;
  }
  * { box-sizing: border-box; margin: 0; padding: 0; }
  html, body { width: 786px; height: 1200px; overflow: hidden; background: var(--page); }
  .canvas { position: relative; width: 786px; height: 1200px; }
  .card {
    position: absolute; left: 31px; width: 724px; overflow: hidden;
    background: var(--paper); box-shadow: 0 2px 8px rgba(0,0,0,0.35);
  }
  .card--front { top: 31px; height: 557px; }
  .card--back { top: 608px; height: 561px; }

  .front-photo {
    position: absolute; inset: 0;
    background: linear-gradient(135deg, #dfe3e6 0%, #f3f4f5 35%, #e8c9c3 52%, #f5f5f5 70%, #e7eaec 100%);
  }
  .front-shapes { position: absolute; inset: 0; }
  .headline { position: absolute; left: 44px; top: 50px; font-family: "Roboto Condensed", sans-serif; color: #fff; }
  .headline__same-day {
    display: block; font-size: 33px; font-weight: 900; font-style: italic; letter-spacing: 5px;
    text-shadow: 0 0 3px var(--navy), 1px 1px 0 var(--navy);
  }
  .headline__service {
    display: block; margin-top: 0; font-size: 29px; font-weight: 700;
    text-shadow: 1px 1px 3px rgba(0,0,0,0.6);
  }
  .specialty {
    position: absolute; left: 484px; top: 112px; width: 232px;
    font-family: "Roboto Condensed", sans-serif; font-weight: 700; font-size: 26px;
    line-height: 37px; color: var(--sky);
  }
  .brand {
    font-family: "Roboto Condensed", sans-serif; font-weight: 700; color: var(--navy); white-space: nowrap;
  }
  .front-contact {
    position: absolute; right: 8px; top: 438px; width: 350px; text-align: center;
  }
  .card--front .brand__name { display: block; font-size: 41px; line-height: 52px; }
  .card--front .brand__phone { display: block; margin-top: 6px; font-size: 35px; line-height: 42px; }
  .front-address {
    position: absolute; left: 33px; top: 517px;
    font-family: "Roboto Condensed", sans-serif; font-weight: 700; font-size: 19px; color: var(--navy);
  }

  .back-photo {
    position: absolute; left: 16px; top: 12px; width: 360px; height: 147px;
    background: linear-gradient(90deg, #d9d4cf 0%, #f1ede9 30%, #f7f7f7 55%, #f0c9c4 75%, #f6f6f6 100%);
  }
  .swoosh { position: absolute; left: 0; top: 0; }
  .pitch {
    position: absolute; left: 30px; top: 180px; width: 330px; text-align: center;
    font-family: "Carlito", sans-serif; color: var(--navy);
  }
  .pitch__body { font-size: 15.5px; line-height: 23px; }
  .pitch__cta { font-size: 15.5px; line-height: 23px; font-weight: 700; font-style: italic; }
  .card--back .brand { text-align: center; }
  .card--back .brand__name { display: block; margin-top: 8px; font-size: 36px; line-height: 48px; }
  .card--back .brand__phone { display: block; margin-top: 4px; font-size: 35px; line-height: 44px; }
  .mailing {
    position: absolute; left: 446px; top: 40px; font-style: normal;
    font-family: "Carlito", sans-serif; font-size: 13.5px; line-height: 19px; color: var(--ink);
  }
</style>
</head>
<body>
<main class="canvas">
  <section class="card card--front">
    <div class="front-photo" role="img" aria-label="Photo of a gloved technician adjusting a denture model on an articulator"></div>
    <svg class="front-shapes" width="724" height="557" viewBox="0 0 724 557" aria-hidden="true">
      <polygon points="0,0 170,0 0,420" fill="var(--tint)"/>
      <polygon points="555,0 724,0 724,40 690,70" fill="var(--tint-strong)"/>
      <polygon points="300,557 690,300 724,330 724,557" fill="var(--tint-strong)"/>
    </svg>
    <div class="headline">
      <span class="headline__same-day">SAME DAY</span>
      <span class="headline__service">RELINES &amp; REPAIRS!</span>
    </div>
    <p class="specialty">We specialize in removable dentures and partials.</p>
    <div class="front-contact">
      <p class="brand brand__name">Velmoran Dental Lab</p>
      <p class="brand brand__phone">(708) 555-0142</p>
    </div>
    <p class="front-address">4870 N Corbett Ave, Worth, IL 60482</p>
  </section>

  <section class="card card--back">
    <div class="back-photo" role="img" aria-label="Photo of a smiling senior couple beside a set of full dentures"></div>
    <svg class="swoosh" width="724" height="561" viewBox="0 0 724 561" aria-hidden="true">
      <defs>
        <linearGradient id="swoosh-fill" x1="0" y1="0" x2="1" y2="0">
          <stop offset="0" stop-color="#0e5fa8"/>
          <stop offset="0.5" stop-color="#3aa6e4"/>
          <stop offset="1" stop-color="#0d4f93"/>
        </linearGradient>
      </defs>
      <path d="M356,0 L418,0 C440,120 420,300 388,472 L371,472 C392,300 395,120 356,0 Z" fill="url(#swoosh-fill)"/>
    </svg>
    <div class="pitch">
      <p class="pitch__body">There’s no acceptable way to cut corners when working with dentures. That’s why we don’t. Turn to Velmoran Dental Lab for removables solutions - for high quality work at reasonable prices.</p>
      <p class="pitch__cta">Call us to discuss your first case!</p>
      <p class="brand brand__name">Velmoran Dental Lab</p>
      <p class="brand brand__phone">(708) 555-0142</p>
    </div>
    <address class="mailing">
      Velmoran Dental Lab<br>
      4870 N Corbett Ave<br>
      Worth, IL 60482
    </address>
  </section>
</main>
</body>
</html>
```